Brindle Capital and Investments

Create a simple business card design using the logos attached. Make it similar but not exact to the reference photo. Brand guidelines are also included.

```html
<!DOCTYPE html>
<html lang="en">
<head>
<meta charset="utf-8">
<title>Brindle Capital – Business Card</title>
<link rel="stylesheet" href="https://fonts.googleapis.com/css2?family=Montserrat:wght@400;500;700;800&display=swap">
<style>
  :root {
    --navy: #0c1738;
    --navy-deep: #08112b;
    --navy-light: #16275a;
    --rust: #a24e12;
    --white: #ffffff;
    --stage: #e9e6e2;
    --ink-soft: #1a2447;
  }
  * { box-sizing: border-box; margin: 0; padding: 0; }
  html, body {
    width: 1200px; height: 977px; overflow: hidden;
    background: var(--stage);
    font-family: "Montserrat", sans-serif;
  }
  .canvas { position: relative; width: 1200px; height: 977px; }

  .card {
    position: absolute;
    width: 560px; height: 320px;
    border-radius: 18px;
    overflow: hidden;
    box-shadow: 0 10px 28px rgba(0,0,0,0.18);
  }

  /* Front */
  .card-front {
    left: 90px; top: 90px;
    background: var(--navy);
    color: var(--white);
  }
  .front-pattern {
    position: absolute; inset: 0;
    background: linear-gradient(120deg, var(--navy-light) 0%, var(--navy) 45%, var(--navy-deep) 100%);
  }
  .front-content {
    position: relative; height: 100%;
    display: flex; flex-direction: column; align-items: center; justify-content: center;
  }
  .card-front .wordmark {
    font-weight: 800; font-size: 44px; letter-spacing: 3px;
    text-transform: uppercase; color: var(--white);
    text-align: center; line-height: 1.05;
  }
  .card-front .tagline { margin-top: 46px; font-size: 14px; color: var(--white); }
  .tagline strong { font-weight: 800; }

  /* Back */
  .card-back {
    left: 550px; top: 560px;
    background: var(--white);
  }
  .back-symbol {
    position: absolute; right: 0; top: 0;
    width: 260px; height: 100%;
    background: linear-gradient(160deg, rgba(162,78,18,0.30) 0%, rgba(162,78,18,0.12) 45%, rgba(12,23,56,0.28) 100%);
  }
  .back-content { position: relative; padding: 28px 40px; width: 320px; }
  .card-back .edge-tab {
    position: absolute; left: 0; top: 190px;
    width: 10px; height: 60px; background: var(--navy);
  }
  .card-back .wordmark {
    font-weight: 800; font-size: 30px; letter-spacing: 3px;
    text-transform: uppercase; color: var(--navy); line-height: 1.05;
  }
  .person { margin-top: 16px; }
  .person-name {
    font-weight: 500; font-size: 21px; color: var(--navy);
    text-transform: uppercase; letter-spacing: 0.5px; line-height: 1.2;
  }
  .person-role { font-size: 13px; color: var(--rust); margin-top: 1px; }

  .contact { list-style: none; margin-top: 12px; }
  .contact li {
    display: flex; align-items: flex-start; gap: 10px;
    font-size: 11.5px; color: var(--ink-soft); line-height: 1.42;
  }
  .contact svg { width: 11px; height: 11px; margin-top: 3px; flex: none; fill: var(--rust); }
  .contact .stack { display: flex; flex-direction: column; }
</style>
</head>
<body>
<main class="canvas">

  <section class="card card-front" aria-label="Card front">
    <div class="front-pattern" role="img" aria-label="Faint repeating brand symbol pattern on navy"></div>
    <div class="front-content">
      <div class="wordmark">Brindle<br>Capital</div>
      <p class="tagline"><strong>Real</strong> investment</p>
    </div>
  </section>

  <section class="card card-back" aria-label="Card back">
    <div class="back-symbol" role="img" aria-label="Large brand symbol in rust and navy, cropped at the card edge"></div>
    <div class="edge-tab"></div>
    <div class="back-content">
      <div class="wordmark">Brindle<br>Capital</div>

      <div class="person">
        <p class="person-name">Marcus Hale</p>
        <p class="person-role">Managing Director</p>
      </div>

      <ul class="contact">
        <li>
          <svg viewBox="0 0 12 12"><path d="M6 0a4 4 0 0 0-4 4c0 3 4 8 4 8s4-5 4-8a4 4 0 0 0-4-4zm0 5.5A1.5 1.5 0 1 1 6 2.5a1.5 1.5 0 0 1 0 3z"/></svg>
          <span class="stack"><span>Your Street Address Here</span><span>State, Country, Zip 12345</span></span>
        </li>
        <li>
          <svg viewBox="0 0 12 12"><path d="M2.5 0.5l2 2-1 1.5a7 7 0 0 0 4.5 4.5l1.5-1 2 2-1.5 2C5 11 1 7 0.5 2z"/></svg>
          <span>(123) 456-7890 / Direct</span>
        </li>
        <li>
          <svg viewBox="0 0 12 12"><path d="M3 0h6v12H3zM4 1.5v8h4v-8zM5.5 10.2h1v0.9h-1z"/></svg>
          <span>(123) 456-7890 / Cell</span>
        </li>
        <li>
          <svg viewBox="0 0 12 12"><path d="M3 0h6v3H3zM1 4h10v5H9v3H3V9H1zM4 8v3h4V8z"/></svg>
          <span>(123) 456-7890 / Fax</span>
        </li>
        <li>
          <svg viewBox="0 0 12 12"><path d="M0 2h12v8H0zM1 3l5 3.5L11 3v-0.2H1z"/></svg>
          <span>info@brindlecapital.com</span>
        </li>
        <li>
          <svg viewBox="0 0 12 12"><circle cx="6" cy="6" r="5.5"/></svg>
          <span>brindlecapital.com</span>
        </li>
      </ul>
    </div>
  </section>

</main>
</body>
</html>
```